Orchard Pulse Bottle Label

We need a new label design for our juice bottles. The name of our company is Orchard Pulse. We are looking for a modification rather than a complete redesign.
If you look at our website www.orchardpulse-example.com you will see the bottles/labels that we use. We are looking for the next generation of this label. A clean/modern look but something that looks more professional. We want to use the same colors and the same juice man logo other than that we are open to new concepts.
Our competitors are squeeze barn and meadowcup juice. Our goal is to have a label that will stand up to their labels and look just as professional.
Thanks in advance.
Ted Varnock

```html
<!DOCTYPE html>
<html lang="en">
<head>
<meta charset="utf-8">
<title>Orchard Pulse Bottle Label – F1 Orange</title>
<link rel="stylesheet" href="https://fonts.googleapis.com/css2?family=Exo+2:ital,wght@0,300;0,400;0,600;1,600&display=swap">
<style>
  :root {
    --page-bg: #ffffff;
    --cream-light: #fbf5dc;
    --cream-deep: #f1e1b6;
    --green-dark: #168236;
    --green-light: #95c11f;
    --flavour-red: #e23011;
    --brand-green: #12873a;
    --white: #ffffff;
    --runner-red: #d83a1c;
    --runner-orange: #f0a020;
    --runner-green: #8cc43c;
  }
  html, body {
    margin: 0;
    width: 1200px;
    height: 1200px;
    overflow: hidden;
    background: var(--page-bg);
  }
  .canvas {
    position: relative;
    width: 1200px;
    height: 1200px;
  }
  .bottle-label {
    position: absolute;
    left: 330px;
    top: 27px;
    width: 540px;
    height: 1146px;
    box-shadow: 0 6px 24px rgba(0,0,0,0.12);
  }
  .brand-name {
    font-family: "Exo 2", sans-serif;
    font-weight: 600;
    font-size: 50px;
    fill: var(--brand-green);
  }
  .tagline {
    font-family: "Exo 2", sans-serif;
    font-style: italic;
    font-weight: 600;
    font-size: 18.5px;
    letter-spacing: 0.5px;
    fill: var(--white);
  }
  .web-address {
    font-family: "Exo 2", sans-serif;
    font-style: italic;
    font-weight: 600;
    font-size: 16px;
    fill: var(--white);
  }
  .flavour-code {
    font-family: "Exo 2", sans-serif;
    font-weight: 300;
    font-size: 54px;
    fill: var(--white);
  }
  .flavour-name {
    font-family: "Exo 2", sans-serif;
    font-weight: 400;
    font-size: 38px;
    letter-spacing: 2px;
    fill: var(--white);
  }
</style>
</head>
<body>
<main class="canvas">
  <svg class="bottle-label" viewBox="0 0 450 955" xmlns="http://www.w3.org/2000/svg" aria-label="Orchard Pulse F1 Orange bottle label">
    <defs>
      <linearGradient id="cream-field" x1="0" y1="0" x2="0" y2="1">
        <stop offset="0" stop-color="var(--cream-light)"/>
        <stop offset="1" stop-color="var(--cream-deep)"/>
      </linearGradient>
      <radialGradient id="runner-tones" cx="0.5" cy="0.5" r="0.55">
        <stop offset="0" stop-color="var(--runner-red)" stop-opacity="0.55"/>
        <stop offset="0.5" stop-color="var(--runner-orange)" stop-opacity="0.35"/>
        <stop offset="1" stop-color="var(--runner-green)" stop-opacity="0"/>
      </radialGradient>
    </defs>

    <rect class="label-field" x="0" y="0" width="450" height="955" fill="url(#cream-field)"/>

    <ellipse class="runner-illustration" role="img" aria-label="Running figure built from fruits and vegetables"
             cx="250" cy="250" rx="160" ry="165" fill="url(#runner-tones)"/>

    <polygon class="band band-dark" points="0,735 450,265 450,345 0,815" fill="var(--green-dark)"/>
    <polygon class="band band-light" points="0,815 450,345 450,420 0,890" fill="var(--green-light)"/>

    <text class="brand-name" transform="translate(62,650) rotate(-46.2)" textLength="330" lengthAdjust="spacingAndGlyphs">Orchard Pulse</text>
    <text class="tagline" transform="translate(22,790) rotate(-46.2)">FRESH JUICE DELIVERED DIRECTLY TO YOUR DOOR</text>
    <text class="web-address" transform="translate(252,604) rotate(-46.2)">www.orchardpulse-example.com</text>

    <g class="flavour-badge">
      <polygon points="0,955 450,955 228,642" fill="var(--flavour-red)"/>
      <text class="flavour-code" x="228" y="798" text-anchor="middle">F1</text>
      <g class="badge-divider" fill="var(--white)">
        <rect x="160" y="827" width="50" height="1.6"/>
        <rect x="246" y="827" width="50" height="1.6"/>
        <polygon points="228,818 230.6,825 238,825 232,829.5 234.3,837 228,832.5 221.7,837 224,829.5 218,825 225.4,825"/>
      </g>
      <text class="flavour-name" x="228" y="888" text-anchor="middle">ORANGE</text>
    </g>
  </svg>
</main>
</body>
</html>
```